Business Card for Graphic Design Firm

This project is for a new graphic design firm based in New Jersey called Velmoric. We outsource graphic design and marketing jobs. We want to communicate that this is a professional company but it as well creative and artistic. This card may be used as a horizontal double sided paper card or a vertical single sided translucent card so feel free to submit designs in whichever format or both.
Updates

Reason: Extending the deadline because I'm not exactly satisfied with the designs so far.

Please view the updated project brief

Target Market(s)

Adults aged 25-60

Industry/Entity Type

Graphic Design

Font styles to use
Serif
Sans Serif

Requirements
Nice to have
• Maybe a triangular pattern around the edges similar to our logo

```html
<!DOCTYPE html>
<html lang="en">
<head>
<meta charset="utf-8">
<title>Velmoric – Business Card</title>
<link href="https://fonts.googleapis.com/css2?family=Ubuntu:wght@400;500;700&display=swap" rel="stylesheet">
<style>
  :root {
    --backdrop: #8e8e8e;
    --card-white: #f4f4f2;
    --card-black: #050505;
    --brand-grey: #8c8c8c;
    --text-light: #f2f2f2;
    --cyan: #29a9df;
    --blue: #1a7fc1;
    --red: #d9143f;
    --orange: #ef8a12;
    --yellow: #f6c400;
  }
  * { box-sizing: border-box; margin: 0; padding: 0; }
  html, body { width: 1200px; height: 1000px; overflow: hidden; }
  body {
    background: var(--backdrop);
    font-family: "Ubuntu", sans-serif;
    position: relative;
  }
  .card {
    position: absolute;
    left: 250px;
    width: 700px;
    height: 400px;
    overflow: hidden;
  }
  .card--front { top: 60px; background: var(--card-white); }
  .card--back  { top: 540px; background: var(--card-black); }

  .color-band {
    position: absolute;
    height: 24px;
    background: linear-gradient(90deg, var(--cyan), var(--red) 14%, var(--yellow) 28%, var(--cyan) 42%, var(--blue) 52%, var(--red) 64%, var(--orange) 76%, var(--cyan) 90%, var(--blue));
  }

  .wordmark {
    position: absolute;
    color: var(--brand-grey);
    font-weight: 500;
    letter-spacing: 0.12em;
    text-transform: uppercase;
    white-space: nowrap;
    display: flex;
    align-items: center;
    gap: 16px;
    line-height: 1;
  }
  .wordmark__square { background: var(--brand-grey); display: inline-block; flex: none; }

  /* front */
  .card--front .wordmark { right: 50px; top: 70px; font-size: 36px; }
  .front__dark {
    position: absolute; left: 0; right: 0; bottom: 0; top: 150px;
    background: var(--card-black);
  }
  .front__name-panel {
    position: absolute; left: 370px; right: 0; top: 132px; height: 90px;
    background: var(--card-black);
  }
  .card--front .color-band--left  { left: 0; top: 150px; width: 370px; }
  .card--front .color-band--right { left: 370px; top: 222px; width: 330px; }

  .holder {
    position: absolute; right: 40px; top: 150px; text-align: right; color: var(--text-light);
  }
  .holder__name { font-size: 20px; font-weight: 700; letter-spacing: 0.02em; }
  .holder__role { font-size: 16px; margin-top: 2px; }

  .contact {
    position: absolute; color: var(--text-light); font-size: 17px;
    display: flex; align-items: center; gap: 16px; white-space: nowrap;
  }
  .contact svg { width: 20px; height: 20px; fill: var(--text-light); flex: none; }

  /* back */
  .card--back .color-band { left: 0; top: 250px; width: 370px; }
  .card--back .wordmark { right: 60px; top: 300px; font-size: 44px; }
</style>
</head>
<body>

<section class="card card--front" aria-label="Card front">
  <div class="front__dark"></div>
  <div class="front__name-panel"></div>
  <div class="color-band color-band--left" role="img" aria-label="Band of coloured triangles"></div>
  <div class="color-band color-band--right" role="img" aria-label="Band of coloured triangles"></div>

  <div class="wordmark"><span class="wordmark__square" style="width:26px;height:26px"></span>Velmoric</div>

  <div class="holder">
    <p class="holder__name">CARD HOLDER NAME</p>
    <p class="holder__role">Designation</p>
  </div>

  <p class="contact" style="left:60px;top:200px">
    <svg viewBox="0 0 20 20"><path d="M10 2 1 10h3v8h5v-5h2v5h5v-8h3z"/></svg>your street address
  </p>
  <p class="contact" style="left:60px;top:240px">
    <svg viewBox="0 0 20 20"><path d="M5 1c1 0 2 3 2.5 4.5S6 8 6 8c1 2.5 3.5 5 6 6 0 0 1-1.5 2.5-1.5S19 14 19 15s-2 4-4 4C8 19 1 12 1 5c0-2 3-4 4-4z"/></svg>555-204-3178
  </p>
  <p class="contact" style="left:410px;top:280px">
    <svg viewBox="0 0 20 20"><path d="M1 4h18v12H1z" fill="none" stroke="#f2f2f2" stroke-width="1.6"/><path d="M1 4l9 7 9-7" fill="none" stroke="#f2f2f2" stroke-width="1.6"/></svg>555-204-3178
  </p>
  <p class="contact" style="left:410px;top:320px">
    <svg viewBox="0 0 20 20"><circle cx="10" cy="10" r="8" fill="none" stroke="#f2f2f2" stroke-width="1.8"/></svg>lucapirelli@mailbox.ca
  </p>
</section>

<section class="card card--back" aria-label="Card back">
  <div class="color-band" role="img" aria-label="Band of coloured triangles"></div>
  <div class="wordmark"><span class="wordmark__square" style="width:30px;height:30px"></span>Velmoric</div>
</section>

</body>
</html>
```